User profile management app in Bootstrap & AngularJS

We have a single page web app with front end built on AngularJS and Bootstrap. There is a navbar on top and about 10 different views (user profile view, user profile edit, update-able list of items, help section, ...). At this point the app has functionality but no graphics or thought-out layout.

Need a designer to take the existing HTML, CSS (or even JS) files and modify and expand them to make the app look good. Find the existing HTML and JS files for the client attached. You'll need to download angular, bootstrap and ng-map libraries separately.

You can experience the code live at https://design.tovq.net/tovqportal.html

The templates provided are text-only but the result should contain a few icons for better visual experience. Some suggested areas for images include device types (email, cell phone, pager, landline phone, ...), status indicators (true/false, on/off, enabled/disabled, ...), navigation (expand/collapse, previous page/next page, ...), file download, CRUD management (add, edit, delete), help popups, etc

The resulting design and code should be mobile-friendly and handicap-accessible (Section 508 compliant).

Font desired: Univers family but not required, otherwise Arial
Only use color from the list provided in the attached file. Colors should not indicate a specific meaning and the whole design should be primarily blue (RGB R0 G103 B198) and white themed.

Allow for banner somewhere on top of page - about 530 x 100 pixels. Allow for a footer with an image on the left and 2-3 sentences of text (copyright, disclaimer, etc).
Updates

Target Market(s)

general public, design for simplicity and ease of use

Industry/Entity Type

Cell Phone

Coding

Coded - Design and coding required

Number of Pages Required

5+ page

Font styles to use
Sans Serif
Other font styles liked:
• Univers family preferred not required otw Arial

Requirements
Must have
• Use blue (RGB R0 G103 B198) and white theme. Must be mobile friendly and handicap-enabled.
• Icons: Use the three stroke weights; light, medium, bold.
• Icons can be designed as outlines or solid silhouettes in two-dimensional form. Icons must be recognizable to a majority of the intended audience. Avoid fine lines and overly complex imagery.

```html
<!DOCTYPE html>
<html lang="en">
<head>
<meta charset="utf-8">
<title>User Profile</title>
<link rel="stylesheet" href="https://fonts.googleapis.com/css2?family=Arimo:wght@400;700&family=Source+Sans+3:wght@400;600;700&display=swap">
<style>
  :root {
    --brand-blue: #0070b2;
    --white: #ffffff;
    --page-bg: #ffffff;
    --panel-head: #5c5c5c;
    --panel-border: #cfcfcf;
    --panel-body: #fcfcfc;
    --row-line: #d6d6d6;
    --table-head: #dff3fb;
    --row-alt: #f3f3f3;
    --text: #3f3f3f;
    --text-strong: #333333;
  }
  * { box-sizing: border-box; margin: 0; padding: 0; }
  html, body {
    width: 1200px; height: 1119px; overflow: hidden;
    background: var(--page-bg);
    font-family: "Source Sans 3", Arial, sans-serif;
    color: var(--text);
  }
  .navbar {
    height: 55px; background: var(--brand-blue);
    display: flex; align-items: center;
    font-family: Arimo, Arial, sans-serif; color: var(--white);
    position: relative;
  }
  .navbar .brand { position: absolute; left: 83px; font-weight: 700; font-size: 17px; }
  .navbar .nav-link { position: absolute; font-size: 17.5px; color: var(--white); text-decoration: none; }
  .panel {
    position: absolute; left: 83px; width: 1040px;
    border: 1px solid var(--panel-border); border-radius: 4px;
    background: var(--panel-body); overflow: hidden;
  }
  .panel-head {
    height: 56px; background: var(--panel-head); color: var(--white);
    display: flex; align-items: center; padding-left: 23px; gap: 9px;
    font-family: Arimo, Arial, sans-serif; font-weight: 700; font-size: 17.5px;
  }
  .panel-head svg { fill: var(--white); }
  .profile-list {
    position: absolute; left: 18px; top: 81px; width: 999px; height: 326px;
    border: 1px solid var(--row-line); border-radius: 5px; background: var(--white);
  }
  .profile-row {
    height: 45px; border-bottom: 1px solid var(--row-line);
    display: flex; align-items: center; font-size: 16.5px;
  }
  .profile-row .label { width: 150px; text-align: right; }
  .profile-row .value { margin-left: 23px; }
  .data-table {
    position: absolute; left: 22px; width: 994px; border-collapse: collapse; font-size: 16.5px;
  }
  .data-table th, .data-table td { height: 55px; text-align: left; padding: 0; }
  .data-table thead tr { background: var(--table-head); }
  .data-table th { font-weight: 700; color: var(--text); }
  .data-table td { color: var(--text-strong); }
  .data-table tbody tr:nth-child(even) { background: var(--row-alt); }
  .data-table .c1 { padding-left: 64px; width: 475px; }
  .data-table .c2 { width: 343px; }
</style>
</head>
<body>
  <nav class="navbar" aria-label="Main">
    <span class="brand">BRAND</span>
    <a class="nav-link" href="#" style="left:204px">Home</a>
    <a class="nav-link" href="#" style="left:290px">Devices</a>
    <a class="nav-link" href="#" style="left:391px">Locations</a>
    <a class="nav-link" href="#" style="left:505px">Profile</a>
    <a class="nav-link" href="#" style="left:594px">Subscriptions</a>
    <a class="nav-link" href="#" style="left:738px">Alert Log</a>
    <a class="nav-link" href="#" style="left:847px">Help</a>
  </nav>

  <section class="panel profile-panel" style="top:80px;height:429px">
    <h2 class="panel-head">
      <svg width="14" height="16" viewBox="0 0 14 16" aria-hidden="true"><circle cx="7" cy="4.5" r="4"/><path d="M0 16c0-5 3-7 7-7s7 2 7 7z"/></svg>
      User Profile
    </h2>
    <div class="profile-list">
      <div class="profile-row"><span class="label">Firstname :</span><span class="value">Paul</span></div>
      <div class="profile-row"><span class="label">Last Name :</span><span class="value">Harlow</span></div>
      <div class="profile-row"><span class="label">E-mail :</span><span class="value">admin</span></div>
      <div class="profile-row"><span class="label">City :</span><span class="value">Gotham</span></div>
      <div class="profile-row"><span class="label">State :</span><span class="value">American Samoa</span></div>
      <div class="profile-row"><span class="label">Languages :</span><span class="value">French , Spanish</span></div>
    </div>
  </section>

  <section class="panel groups-panel" style="top:543px;height:187px">
    <h2 class="panel-head">
      <svg width="20" height="16" viewBox="0 0 20 16" aria-hidden="true"><circle cx="10" cy="4" r="3.3"/><circle cx="4" cy="5" r="2.5"/><circle cx="16" cy="5" r="2.5"/><path d="M4.5 15c0-4 2.5-6 5.5-6s5.5 2 5.5 6z"/><path d="M0 13c0-3 2-4.5 4-4.5 1 0 1.6.3 2 .6-1.3 1-2 2.3-2.2 3.9z"/><path d="M20 13c0-3-2-4.5-4-4.5-1 0-1.6.3-2 .6 1.3 1 2 2.3 2.2 3.9z"/></svg>
      Groups
    </h2>
    <table class="data-table" style="top:79px">
      <thead><tr><th class="c1">Group Name</th><th class="c2">Category</th><th>Type</th></tr></thead>
    </table>
  </section>

  <section class="panel devices-panel" style="top:766px;height:286px">
    <h2 class="panel-head">
      <svg width="12" height="18" viewBox="0 0 12 18" aria-hidden="true"><path d="M2 0h8a2 2 0 0 1 2 2v14a2 2 0 0 1-2 2H2a2 2 0 0 1-2-2V2a2 2 0 0 1 2-2zm0 3v10h8V3zm4 11.2a1.2 1.2 0 1 0 0 2.4 1.2 1.2 0 0 0 0-2.4z"/></svg>
      Devices
    </h2>
    <table class="data-table" style="top:79px">
      <thead><tr><th class="c1">Device Identifier</th><th class="c2">Delivery Channel</th><th>Status</th></tr></thead>
      <tbody>
        <tr><td class="c1">paulharlow@kestrelmail.com</td><td class="c2">E-mail account</td><td>Enabled</td></tr>
        <tr><td class="c1">Lumo-Grid@kestrelmail.com</td><td class="c2">E-mail account</td><td>Enabled</td></tr>
      </tbody>
    </table>
  </section>
</body>
</html>
```